Web Page Design for Major Airline Consolidator

We need a new design for an airline consolidator based out of NY. We'd really like to get the design as quickly as possible.

Here is a *very* rough mockup of what the site could look like, along with 3 main competitor's sites. Needless to say, they want a design that looks much better than their competitors. Please note that the mockup is an idea only, feel free to enhance / improve upon it.

Mockup - https://plankrig.example/tolvemark/QHRnPzKw

Competitors:
- http://www.trelvan.example/
- http://www.munderbline.example/home2.html
- https://www.prosbek.example/index.php

Target Market(s)

target markets are identified in the mockup

Industry/Entity Type

Airline

Number of Pages Required

1 page

Requirements
Must have
• need space on the left side for a travel request form which is missing in the mockup. Form should have standard air booking fields (to, from, date arrival & departure, travel class, etc).

```html
<!DOCTYPE html>
<html lang="en">
<head>
<meta charset="utf-8">
<title>Brookfen Tours – Airline Consolidation</title>
<link rel="stylesheet" href="https://fonts.googleapis.com/css2?family=Open+Sans:wght@400;600;700&display=swap">
<style>
:root{
  --green:#1d6a45;
  --green-dark:#17553a;
  --green-card:rgba(28,104,68,.82);
  --blue:#3aa3d8;
  --btn-blue:#3aa6dc;
  --ink:#2b2b2b;
  --muted:#555;
  --line:#444;
  --grey-band:#ececec;
  --white:#fff;
}
*{box-sizing:border-box;margin:0;padding:0}
html,body{width:680px;height:1200px;overflow:hidden;background:var(--white)}
body{font-family:"Open Sans",Arial,sans-serif;color:var(--ink);position:relative}
.abs{position:absolute}

/* top utility bar */
.top-rule{left:0;top:0;width:680px;height:4px;background:#111}
.utility-bar{left:353px;top:0;width:327px;height:15px;background:#111;color:#fff;font-size:6px;display:flex;align-items:center}
.utility-bar .auth{margin-left:27px}
.utility-bar .auth span+span{border-left:1px solid #fff;margin-left:5px;padding-left:5px}
.utility-bar .search{margin-left:60px;width:58px;height:7px;border:1px solid #ccc;border-radius:2px}
.utility-bar .lang{margin-left:47px}

/* header */
.brand{left:64px;top:18px}
.brand-name{font-size:22px;font-weight:600;color:#555;display:flex;align-items:center;gap:6px;line-height:1}
.brand-name i{width:14px;height:14px;background:#666;display:inline-block}
.brand-tag{font-size:7px;color:#555;margin-left:20px;margin-top:2px}
.contact{top:37px;font-size:11px;color:#555;display:flex;align-items:center;gap:8px}
.contact.email{left:353px}
.contact.phone{left:529px}
.nav-line{left:64px;width:551px;height:1px;background:#999}
.main-nav{left:65px;top:83px;font-size:7.6px;display:flex;gap:10.5px;color:#222}

/* hero */
.hero{left:0;top:102px;width:680px;height:448px;background:linear-gradient(180deg,#8fb8c9 0%,#b9d3de 35%,#d5e6ec 60%,#a7c4cf 100%)}
.quote-form{left:74px;top:120px;width:171px;height:238px;background:var(--green);border-radius:3px;box-shadow:0 2px 4px rgba(0,0,0,.35)}
.quote-form h2{position:absolute;left:20px;top:19px;width:131px;height:29px;background:#fff;font-size:14px;font-weight:400;text-align:center;line-height:29px;box-shadow:0 2px 2px rgba(0,0,0,.4)}
.field{position:absolute;left:22px;color:#fff;font-size:10px;font-weight:600}
.field span{position:absolute;top:-1px;height:14px;background:#fff;border-radius:2px}
.submit{position:absolute;left:53px;top:210px;width:64px;height:16px;background:var(--btn-blue);color:#fff;font-size:10px;font-weight:600;text-align:center;line-height:16px;border-radius:2px}
.hero-title{left:258px;top:124px;font-size:24px;font-weight:700;color:#fff;line-height:29px;text-shadow:0 1px 3px rgba(0,0,0,.4)}
.checks{left:258px;top:186px;font-size:8.3px;color:var(--green);line-height:17.3px;list-style:none}
.checks li{padding-left:15px;position:relative}
.checks li svg{position:absolute;left:0;top:4px}
.learn-more{left:262px;top:301px;width:102px;height:27px;background:var(--green-dark);color:#fff;font-size:14px;font-weight:600;text-align:center;line-height:27px;border-radius:2px}
.agency-card{top:389px;width:172px;height:161px;background:var(--green-card);color:#fff}
.agency-card h3{font-size:11.5px;font-weight:600;text-align:center;margin:11px 8px 0;padding-bottom:3px;border-bottom:1px solid rgba(255,255,255,.6)}
.agency-card .sub{font-size:7px;text-align:center;margin-top:8px}
.agency-card ul{list-style:none;font-size:7px;line-height:12px;margin:10px 0 0 12px;width:82px}
.agency-card .photo{position:absolute;left:89px;top:58px;width:70px;height:48px;background:linear-gradient(180deg,#8fb2c4,#6a8a5a 60%,#4d7a3b)}
.join{position:absolute;left:46px;top:126px;width:66px;height:16px;background:var(--btn-blue);font-size:7px;font-weight:600;text-align:center;line-height:16px;border-radius:2px}

/* corporate section */
.corp{left:0;top:550px;width:680px;height:200px;background:linear-gradient(90deg,#fff,#f4f6f8 60%,#fff)}
.corp h2{position:absolute;left:76px;top:29px;font-size:11.5px;font-weight:400}
.corp p{position:absolute;left:76px;font-size:8.5px;line-height:10.5px;width:250px}
.corp .cta{position:absolute;left:77px;top:148px;width:177px;height:20px;background:var(--btn-blue);color:#fff;font-size:8.8px;line-height:20px;padding-left:7px;border-radius:2px}
.corp-photo{left:364px;top:558px;width:244px;height:186px;background:linear-gradient(135deg,#e8eef2,#b9c6cf 55%,#2d3440);clip-path:polygon(18% 0,100% 0,82% 100%,0 100%)}

/* group travel */
.group{left:0;top:750px;width:680px;height:184px;background:var(--blue);color:#fff}
.group h2{position:absolute;width:100%;top:26px;text-align:center;font-size:12.5px;font-weight:600}
.group .photo{position:absolute;top:64px;width:128px;height:86px}
.group h4{position:absolute;top:71px;font-size:7px;font-weight:600}
.group p{position:absolute;top:84px;width:100px;font-size:5.6px;line-height:8.4px}
.group .contact-btn{position:absolute;top:154px;width:60px;height:15px;background:var(--green-dark);font-size:6px;line-height:15px;text-align:center;border-radius:2px}

/* ceo */
.ceo-photo{left:119px;top:965px;width:112px;height:113px;background:linear-gradient(180deg,#c79a5f,#8a6a4b 50%,#3c4350)}
.ceo-quote{left:242px;top:964px;width:310px;font-size:7.8px;line-height:11px}
.ceo-name{left:243px;top:998px;font-size:10px}
.info-box{top:1026px;width:85px;height:53px;border:2px solid var(--green);padding:2px 4px;font-size:5.4px;line-height:7.4px;color:#666}
.info-box h5{font-size:7px;font-weight:400;color:#444;margin-bottom:2px}
.info-box b{color:var(--btn-blue);font-weight:400}

/* members + footer */
.members{left:0;top:1108px;width:680px;height:62px;background:var(--grey-band)}
.members h3{position:absolute;left:102px;top:21px;font-size:14px;font-weight:400;color:#333}
.badge{position:absolute;background:#a8a8a8}
.footer{left:0;top:1170px;width:680px;height:30px;background:var(--green-dark);color:#fff;font-size:9.5px}
.footer span{position:absolute;left:66px;top:8px}
.social{position:absolute;top:7px;width:16px;height:16px;border-radius:50%;background:#111}
</style>
</head>
<body>

<div class="abs top-rule"></div>
<div class="abs utility-bar">
  <div class="auth"><span>Log in</span><span>Register</span></div>
  <div class="search"></div>
  <div class="lang">EN ▾</div>
</div>

<div class="abs brand">
  <div class="brand-name"><i></i>Brookfen Tours</div>
  <div class="brand-tag">The Professional's choice since 1974</div>
</div>

<div class="abs contact email">
  <svg width="15" height="11" viewBox="0 0 15 11"><rect width="15" height="11" fill="#1d6a45"/><path d="M0 0 L7.5 6 L15 0" stroke="#fff" stroke-width="1.2" fill="none"/></svg>
  info@brookfentours.example
</div>
<div class="abs contact phone">
  <svg width="13" height="13" viewBox="0 0 13 13"><rect width="13" height="13" rx="2" fill="#1d6a45"/><path d="M4 3 L6 3 L6 5 L5 6 Q6 8 7.5 8.5 L8.5 7.5 L10 8 L10 10 Q5 10 3 4 Z" fill="#fff"/></svg>
  888-555-0142
</div>

<div class="abs nav-line" style="top:74px"></div>
<nav class="abs main-nav">
  <span>Home</span><span>Travel Agencies</span><span>Religious &amp; Group Travel</span><span>Corporate Concierge</span><span>Niche Agencies</span><span>Destinations</span><span>About Brookfen</span><span>Restricted Area</span>
</nav>
<div class="abs nav-line" style="top:101px;left:0;width:680px;background:#ccc"></div>

<section class="abs hero" role="img" aria-label="Snow-covered mountain with a parachute floating in the sky"></section>

<form class="abs quote-form">
  <h2>Get a Quote</h2>
  <div class="field" style="top:72px">Name<span style="left:44px;width:87px"></span></div>
  <div class="field" style="top:95px">Email<span style="left:44px;width:87px"></span></div>
  <div class="field" style="top:118px">Depart from<span style="left:69px;width:62px"></span></div>
  <div class="field" style="top:142px">Arrive at<span style="left:69px;width:62px"></span></div>
  <div class="field" style="top:165px">Departure date<span style="left:84px;width:47px"></span></div>
  <div class="field" style="top:188px">Return date<span style="left:84px;width:47px"></span></div>
  <div class="submit">Submit</div>
</form>

<h1 class="abs hero-title">More Than Just<br>Airline Consolidation</h1>
<ul class="abs checks">
  <li><svg width="9" height="8" viewBox="0 0 9 8"><path d="M1 4 L3.5 7 L8 1" stroke="#1d6a45" stroke-width="2" fill="none"/></svg>We're here for our clients!</li>
  <li><svg width="9" height="8" viewBox="0 0 9 8"><path d="M1 4 L3.5 7 L8 1" stroke="#1d6a45" stroke-width="2" fill="none"/></svg>Over 40 years in business</li>
  <li><svg width="9" height="8" viewBox="0 0 9 8"><path d="M1 4 L3.5 7 L8 1" stroke="#1d6a45" stroke-width="2" fill="none"/></svg>Locations across the USA</li>
  <li><svg width="9" height="8" viewBox="0 0 9 8"><path d="M1 4 L3.5 7 L8 1" stroke="#1d6a45" stroke-width="2" fill="none"/></svg>50+ air carriers</li>
  <li><svg width="9" height="8" viewBox="0 0 9 8"><path d="M1 4 L3.5 7 L8 1" stroke="#1d6a45" stroke-width="2" fill="none"/></svg>Worldwide + Europe &amp; Middle<br>East travel</li>
</ul>
<div class="abs learn-more">Learn More</div>

<div class="abs agency-card" style="left:73px">
  <h3>Home Based Travel Agents</h3>
  <div class="sub">Find your way to financial freedom!</div>
  <ul><li>•Don't lose another client to the big guys</li><li>•Get more referrals and more customers!</li><li>•Earn more per</li></ul>
  <div class="photo" role="img" aria-label="Suburban house with garden"></div>
  <div class="join">Join Now</div>
</div>
<div class="abs agency-card" style="left:255px">
  <h3>Small Travel Agencies</h3>
  <div class="sub">Accelerate your growth!</div>
  <ul><li>•Don't lose another client to the big guys</li><li>•Get more referrals and more customers!</li><li>•Earn more per</li></ul>
  <div class="photo" role="img" aria-label="Suburban house with garden"></div>
  <div class="join">Join Now</div>
</div>
<div class="abs agency-card" style="left:437px">
  <h3>Corporate Travel Agencies</h3>
  <div class="sub">Earn &amp; retain higher value clients</div>
  <ul><li>•Don't lose another client to the big guys</li><li>•Get more referrals and more customers!</li><li>•Earn more per</li></ul>
  <div class="photo" role="img" aria-label="Suburban house with garden"></div>
  <div class="join">Join Now</div>
</div>

<section class="abs corp" role="region" aria-label="Corporate consolidation">
  <h2>Airline Consolidators for Businesses &amp; Corporations</h2>
  <p style="top:59px">Tired of Travel Headaches? Make Business Travel EASY!</p>
  <p style="top:78px">•Excellent customer service, we staff over 200 agents and have locations in 6 major US cities<br>•Always available<br>•Buy in bulk &amp; save even more!<br>•Save more by going direct to the consolidator!<br>•Your best interests are ours!</p>
  <div class="cta">Experience the difference of Brookfen!</div>
</section>
<div class="abs corp-photo" role="img" aria-label="Call-centre agent with headset and colleagues in an office"></div>

<section class="abs group">
  <h2>Group Travel - Missionary Airfares, HAJJ &amp; Umra Discounted Airfares</h2>
  <div class="photo" style="left:99px;background:linear-gradient(135deg,#6a5a4e,#2e2a2a 60%,#8b7a70)" role="img" aria-label="Family group portrait"></div>
  <h4 style="left:237px">HAJJ Group Travel Rates</h4>
  <p style="left:237px">Lorem ipsum dolor sit amet, consectetur adipisicing elit, sed do eiusmod tempor incididunt ut labore et dolore magna aliqua. Ut enim ad minim.</p>
  <div class="contact-btn" style="left:238px">Contact Us Now</div>
  <div class="photo" style="left:351px;background:linear-gradient(180deg,#5d7a3a,#a48c5a 60%,#6f8a44)" role="img" aria-label="Missionary with children on a village path"></div>
  <h4 style="left:489px">Missionary Travel</h4>
  <p style="left:489px">Lorem ipsum dolor sit amet, consectetur adipisicing elit, sed do eiusmod tempor incididunt ut labore et dolore magna aliqua. Ut enim ad minim.</p>
  <div class="contact-btn" style="left:490px">Contact Us Now</div>
</section>

<div class="abs ceo-photo" role="img" aria-label="Portrait of the company president"></div>
<p class="abs ceo-quote">"Great airfares are only the beginning, exceptional customer service and caring for our clients is what makes us so unique"</p>
<p class="abs ceo-name">- Mr. Delcourt, President &amp; CEO</p>
<div class="abs info-box" style="left:254px"><h5>Our History</h5>Lorem ipsum dolor sit ame consectetur adipisicing elit sed do eiusmod tempor incididunt ut labore et.... <b>[Read More]</b></div>
<div class="abs info-box" style="left:359px"><h5>Our Divisions</h5>Lorem ipsum dolor sit ame consectetur adipisicing elit sed do eiusmod tempor incididunt ut labore et....<b>[Read More]</b></div>
<div class="abs info-box" style="left:464px"><h5>Our Employees</h5>Lorem ipsum dolor sit ame consectetur adipisicing elit sed do eiusmod tempor incididunt ut labore et....<b>[Read More]</b></div>

<section class="abs members">
  <h3>Trusted Members of:</h3>
  <div class="badge" style="left:320px;top:17px;width:58px;height:26px;border-radius:2px"></div>
  <div class="badge" style="left:411px;top:16px;width:37px;height:30px"></div>
  <div class="badge" style="left:484px;top:16px;width:48px;height:30px;border-radius:50%"></div>
</section>

<footer class="abs footer">
  <span>Copyright©brookfentours.example.2014.All Rights Reserved</span>
  <i class="social" style="left:513px"></i>
  <i class="social" style="left:541px"></i>
  <i class="social" style="left:569px"></i>
  <i class="social" style="left:597px"></i>
</footer>

</body>
</html>
```